Bramble Hollow is company name.Handknit&crochet blankets&scarves. Need logo&business ...

I need a design that is eye catching, using yarn and is flowing. I'd like to see colors in aqua (Halvorsen Pike paint HP4817 Merilune) for the yarn and company name. For the text, a dark grey color (Halvorsen Pike HP5308 Velden Ash)

Colors
87cfc7

```html
<!DOCTYPE html>
<html lang="en">
<head>
<meta charset="utf-8">
<title>Bramble Hollow — Business Card</title>
<link href="https://fonts.googleapis.com/css2?family=Maven+Pro:wght@400;500&display=swap" rel="stylesheet">
<style>
  :root {
    --backdrop: #6cc3c3;
    --card: #ffffff;
    --aqua: #40bcbd;
    --ash: #5e6164;
  }
  html, body {
    margin: 0;
    padding: 0;
    width: 1200px;
    height: 1200px;
    overflow: hidden;
    background: var(--backdrop);
    font-family: "Maven Pro", sans-serif;
  }
  .card {
    position: absolute;
    left: 80px;
    top: 303px;
    width: 1040px;
    height: 594px;
    background: var(--card);
  }
  .card-frame {
    position: absolute;
    inset: 26px;
    border: 4px solid var(--aqua);
  }
  .brand {
    position: absolute;
    left: 0;
    right: 0;
    top: 150px;
    display: flex;
    justify-content: center;
    align-items: center;
    gap: 22px;
  }
  .brand-dot {
    width: 46px;
    height: 46px;
    border-radius: 50%;
    background: var(--aqua);
  }
  .brand-name {
    font-size: 66px;
    font-weight: 500;
    letter-spacing: 4px;
    color: var(--aqua);
    text-transform: uppercase;
    line-height: 1;
  }
  .contact {
    position: absolute;
    left: 175px;
    top: 356px;
  }
  .contact-name {
    font-size: 37px;
    font-weight: 500;
    color: var(--aqua);
    margin: 0 0 4px;
    line-height: 1.1;
  }
  .contact-line {
    font-size: 28px;
    color: var(--ash);
    line-height: 37px;
    margin: 0;
  }
  .contact-label {
    color: var(--aqua);
    font-size: 24px;
    margin-right: 8px;
  }
  .divider {
    position: absolute;
    left: 518px;
    top: 365px;
    width: 3px;
    height: 145px;
    background: var(--aqua);
  }
  .offerings {
    position: absolute;
    left: 589px;
    top: 366px;
    margin: 0;
    padding: 0;
    list-style: none;
  }
  .offerings li {
    font-size: 28px;
    color: var(--ash);
    line-height: 37px;
  }
</style>
</head>
<body>
  <div class="card">
    <div class="card-frame"></div>

    <div class="brand">
      <span class="brand-dot"></span>
      <span class="brand-name">Bramble Hollow</span>
    </div>

    <div class="contact">
      <p class="contact-name">Ingrid Callow</p>
      <p class="contact-line"><span class="contact-label">T:</span>+0 123 456 7899</p>
      <p class="contact-line"><span class="contact-label">E:</span>your@email.com</p>
    </div>

    <div class="divider"></div>

    <ul class="offerings">
      <li>Hand Knit &amp; Crochet</li>
      <li>Baby Afghans</li>
      <li>Afghans</li>
      <li>Scarves,Gloves,Hats</li>
    </ul>
  </div>
</body>
</html>
```